Professional & attention grabbing.

A business card design, front and back. I already have a logo I will attach, but I am open to something new as well.
Things to include:
Name:
Title:
Phone:
Email:
Wanting something that is professional but attention grabbing.
Also we do a lot of work using drones on natural gas pipelines (leading the future)if you want to include any of that. I'm open to ideas.
Target Market(s)
Natural gas transmission industry / greenhouse gas mitigation industry
Industry/Entity Type
Business
Contact Information for Business Card
All details have been conveyed above.
Colors
Designer to choose colors to be used in the design.
Look and feel
Each slider illustrates characteristics of the customer's brand and the style your logo design should communicate.

```html
<!DOCTYPE html>
<html lang="en">
<head>
<meta charset="utf-8">
<title>Kestrel Line Surveys – Business Card</title>
<link href="https://fonts.googleapis.com/css2?family=Open+Sans:ital,wght@0,400;0,600;0,700;1,400&display=swap" rel="stylesheet">
<style>
  :root {
    --backdrop: #5b4b3d;
    --paper: #ffffff;
    --ink: #38383b;
    --brand-red: #be1e24;
    --rule: #38383b;
    --on-dark: #ffffff;
  }
  * { margin: 0; padding: 0; box-sizing: border-box; }
  html, body {
    width: 1200px; height: 987px; overflow: hidden;
    background: var(--backdrop);
    font-family: "Open Sans", Arial, sans-serif;
  }
  .stage { position: relative; width: 1200px; height: 987px; }

  .card {
    position: absolute; left: 293px; width: 615px; height: 352px;
    overflow: hidden;
  }
  .card--front { top: 130px; background: var(--paper); }
  .card--back { top: 505px; background: var(--ink); }

  /* front */
  .brand {
    position: absolute; right: 45px; top: 50px;
    display: flex; align-items: center; gap: 14px;
  }
  .brand__square { width: 58px; height: 58px; background: var(--brand-red); }
  .brand__name {
    color: var(--ink); font-weight: 700; font-size: 24px; line-height: 1.05;
    letter-spacing: 0.5px;
  }

  .identity {
    position: absolute; left: 46px; top: 234px;
    display: flex; align-items: baseline; gap: 10px;
  }
  .identity__name { color: var(--brand-red); font-size: 20px; font-weight: 600; }
  .identity__dash { color: var(--brand-red); font-size: 20px; font-weight: 600; }
  .identity__title { color: var(--ink); font-size: 16px; }

  .rule {
    position: absolute; left: 46px; right: 45px; top: 269px;
    height: 1px; background: var(--rule);
  }

  .contacts {
    position: absolute; left: 46px; right: 45px; top: 278px;
    display: flex; justify-content: space-between; align-items: center;
    color: var(--ink); font-size: 15px; list-style: none;
  }
  .contacts li { display: flex; align-items: center; gap: 5px; white-space: nowrap; }
  .contacts svg { width: 14px; height: 14px; fill: var(--brand-red); }

  .band {
    position: absolute; left: 0; right: 0; bottom: 0; height: 16px;
    display: flex;
  }
  .band__red { width: 475px; background: var(--brand-red); }
  .band__dark { flex: 1; background: var(--ink); }

  /* back */
  .back-brand {
    position: absolute; left: 0; right: 0; top: 80px;
    display: flex; flex-direction: column; align-items: center; gap: 22px;
  }
  .back-brand__square { width: 110px; height: 110px; background: var(--brand-red); }
  .back-brand__name {
    color: var(--on-dark); font-weight: 700; font-size: 26px; letter-spacing: 1px;
  }
  .back-web {
    position: absolute; left: 0; right: 0; top: 302px; text-align: center;
    color: var(--on-dark); font-style: italic; font-size: 17px; letter-spacing: 4px;
  }
</style>
</head>
<body>
<main class="stage">
  <section class="card card--front" aria-label="Business card front">
    <div class="brand">
      <span class="brand__square"></span>
      <span class="brand__name">KESTREL LINE<br>SURVEYS</span>
    </div>

    <div class="identity">
      <span class="identity__name">DANA WHITFIELD</span>
      <span class="identity__dash">-</span>
      <span class="identity__title">CEO/FOUNDER</span>
    </div>
    <div class="rule"></div>

    <ul class="contacts">
      <li>
        <svg viewBox="0 0 24 24" aria-hidden="true"><path d="M6.6 10.8a15.1 15.1 0 0 0 6.6 6.6l2.2-2.2c.3-.3.7-.4 1-.2 1.1.4 2.3.6 3.6.6.6 0 1 .4 1 1V20c0 .6-.4 1-1 1A17 17 0 0 1 3 4c0-.6.4-1 1-1h3.5c.6 0 1 .4 1 1 0 1.3.2 2.5.6 3.6.1.3 0 .7-.2 1z"/></svg>
        555 014 2290
      </li>
      <li>
        <svg viewBox="0 0 24 24" aria-hidden="true"><path d="M2 5h20v14H2z M2 5l10 8 10-8" /><path d="M2 6.5l10 7.5 10-7.5V5H2z" fill="#fff"/></svg>
        HELLO@KESTRELLINE.COM
      </li>
      <li>
        <svg viewBox="0 0 24 24" aria-hidden="true"><circle cx="12" cy="12" r="10"/><path d="M2 12h20M12 2c3 3 3 17 0 20M12 2c-3 3-3 17 0 20" stroke="#fff" stroke-width="1.6" fill="none"/></svg>
        WWW.KESTRELLINE.COM
      </li>
    </ul>

    <div class="band"><span class="band__red"></span><span class="band__dark"></span></div>
  </section>

  <section class="card card--back" aria-label="Business card back">
    <div class="back-brand">
      <span class="back-brand__square"></span>
      <span class="back-brand__name">KESTREL LINE SURVEYS</span>
    </div>
    <p class="back-web">www.kestrelline.com</p>
  </section>
</main>
</body>
</html>
```